Brisbane IT support business needs our first facebook page

Hi All,

We are after a new facebook page for our IT solutions and support business.The business name is Marlowe Computer Network Helpdesk, or MCNH for short. We provide a range of solutions and services within the IT space.

I would like to utilize the two colours in our business logo I have uploaded.

```html
<!DOCTYPE html>
<html lang="en">
<head>
<meta charset="utf-8">
<title>Marlowe Computer Network Helpdesk – Facebook Cover</title>
<link rel="stylesheet" href="https://fonts.googleapis.com/css2?family=Arimo:wght@400;700&family=Roboto+Condensed:wght@400&display=swap">
<style>
  :root {
    --orange: #f0892e;
    --orange-light: #f7a65a;
    --orange-deep: #e4761c;
    --navy: #1f4d62;
    --navy-dark: #173c4e;
    --white: #ffffff;
    --frame: #2b2b2b;
    --photo-a: #dfe6ec;
    --photo-b: #8ea6bb;
    --photo-c: #2f4a66;
  }
  html, body {
    margin: 0;
    padding: 0;
    overflow: hidden;
    background: #ffffff;
  }
  .cover {
    position: relative;
    width: 1200px;
    height: 443px;
    overflow: hidden;
    background:
      linear-gradient(115deg, transparent 0 38%, rgba(255,255,255,0.10) 38% 46%, transparent 46% 100%),
      linear-gradient(70deg, transparent 0 20%, rgba(255,255,255,0.08) 20% 30%, transparent 30% 100%),
      radial-gradient(ellipse at 55% 45%, var(--orange-light) 0%, var(--orange) 45%, var(--orange-deep) 100%);
    font-family: "Roboto Condensed", Arial, sans-serif;
  }
  .brand-title {
    position: absolute;
    left: 0;
    top: 6px;
    width: 846px;
    margin: 0;
    text-align: center;
    font-family: "Arimo", Arial, sans-serif;
    font-weight: 700;
    font-size: 38px;
    line-height: 40px;
    color: var(--white);
    letter-spacing: 0.2px;
  }
  .tagline {
    position: absolute;
    left: 0;
    top: 107px;
    width: 762px;
    margin: 0;
    text-align: center;
    font-size: 40px;
    font-weight: 400;
    color: var(--navy);
    letter-spacing: -0.3px;
  }
  .subline {
    position: absolute;
    left: 0;
    top: 158px;
    width: 770px;
    margin: 0;
    text-align: center;
    font-size: 24px;
    color: var(--white);
  }
  .services {
    list-style: none;
    margin: 0;
    padding: 0;
  }
  .service {
    position: absolute;
    left: 368px;
    width: 269px;
    height: 48px;
    background: var(--navy);
    color: var(--white);
    display: flex;
    align-items: center;
    justify-content: center;
    text-align: center;
    font-size: 24px;
    line-height: 22px;
  }
  .service--selection { top: 214px; height: 50px; font-size: 21px; }
  .service--consultancy { top: 300px; }
  .service--support { top: 381px; }
  .logo-card {
    position: absolute;
    left: 35px;
    top: 272px;
    width: 230px;
    height: 180px;
    background: var(--white);
    border: 4px solid var(--frame);
    border-radius: 4px;
    display: flex;
    align-items: center;
    justify-content: center;
    gap: 12px;
  }
  .logo-dot {
    width: 36px;
    height: 36px;
    border-radius: 50%;
    background: var(--orange);
  }
  .logo-name {
    font-family: "Roboto Condensed", Arial, sans-serif;
    font-size: 44px;
    color: var(--navy);
  }
  .photo-frame {
    position: absolute;
    left: 726px;
    top: -162px;
    width: 744px;
    height: 744px;
    border-radius: 50%;
    border: 11px solid var(--navy-dark);
    overflow: hidden;
  }
  .photo {
    width: 100%;
    height: 100%;
    background:
      radial-gradient(circle at 35% 55%, rgba(255,255,255,0.9) 0%, transparent 30%),
      linear-gradient(120deg, var(--photo-a) 0%, var(--photo-b) 45%, var(--photo-c) 100%);
  }
  .pointer {
    position: absolute;
    left: 718px;
    top: 202px;
  }
</style>
</head>
<body>
  <main class="cover">
    <h1 class="brand-title">Marlowe Computer Network<br>Helpdesk</h1>
    <p class="tagline">Better at IT-Better at Business</p>
    <p class="subline">Improve your business</p>

    <ul class="services">
      <li class="service service--selection">Solution Selection and<br>Acquisition</li>
      <li class="service service--consultancy">Consultantsy</li>
      <li class="service service--support">Business Support</li>
    </ul>

    <div class="logo-card">
      <span class="logo-dot"></span>
      <span class="logo-name">MCNH</span>
    </div>

    <svg class="pointer" width="30" height="40" viewBox="0 0 30 40" aria-hidden="true">
      <polygon points="0,20 30,0 30,40" fill="var(--navy-dark)"/>
    </svg>
    <div class="photo-frame">
      <div class="photo" role="img" aria-label="Photo of a business person in a suit reaching toward glowing blue-white interlocking gears"></div>
    </div>
  </main>
</body>
</html>
```